Hypnotherapy- past life regression-life between lives therapist needs a website

I need a website that is enticing and spiritual in its feeling. It needs to have a lot of beautiful nature pictures included. The theme is "Quiet Harbor Path- what might you find....Lessons Solutions Answers"
Because all of us have the answers to living our best life, they are in our subconcious. But not everyone is capable of accessing them. Hypnosis accesses the subconcious and helps to create new neural pathways in the brain which can create new behaviors and responses to situations.
Hypnosis can help with anxiety, pain relief, weight loss, smoking/vaping cessation, self confidence......anything about yourself that you want to change.
Exploration of past lives and life between lives can reveal things related to ones current life. For example, perhaps your fear of deep water is a result of drowning in a past life. Once this has been discovered, it can lead to changes in ones current life.
Almost any personal behavior one wants to change, can be helped through hypnotherapy.
I need a page for testimonials, a place for scheduling (I will have a link to my scheduling app) some information about hypnotherapy.
I am uploading my logo files. My business card will be using the black and gold style, but my website does not have to reflect that. It can be based on the caramel and deep green like full color logo. Earthy, calm colors.
I also like the mock up of my logo on the beach and there was one on a starry night sky that I also liked.
Target Market(s)
men and women ages 25-50
Industry/Entity Type
natural health and wellness, spirituality
Number of Pages Required
4 page
Requirements
Must have
- a page for testimonials, perhaps with a beautiful nature picture with each one, I will have approximately 6. A link to schedule a complimentary intro session, preferably on the first page
Should not have
- no swinging watches or other sterotyped hypnosis symbols

```html
<!DOCTYPE html>
<html lang="en">
<head>
<meta charset="utf-8">
<title>Quiet Harbor Path – Hypnotherapy</title>
<link rel="stylesheet" href="https://fonts.googleapis.com/css2?family=Cinzel:wght@400;600;700&family=Roboto:ital,wght@0,400;0,500;1,400&display=swap">
<style>
:root{
  --olive:#5b5a2c;
  --olive-dark:#45441f;
  --caramel:#e0862a;
  --caramel-soft:#f3c08a;
  --cream:#efede8;
  --ink:#3a3a32;
  --text:#5c5c55;
  --white:#ffffff;
}
*{box-sizing:border-box;margin:0;padding:0}
html,body{width:1200px;height:5108px;overflow:hidden}
body{position:relative;background:var(--white);font-family:'Roboto',sans-serif;color:var(--text)}
.abs{position:absolute}
.heading{font-family:'Cinzel',serif;color:var(--ink);font-weight:600;letter-spacing:1px}
.btn{display:inline-block;background:var(--caramel);color:var(--white);font-family:'Cinzel',serif;font-weight:700;font-size:15px;border-radius:30px;text-align:center;letter-spacing:.5px;white-space:nowrap}
.brand{font-family:'Cinzel',serif;font-weight:700;color:var(--caramel);display:flex;align-items:center;gap:12px}
.brand-dot{width:30px;height:30px;border-radius:50%;background:var(--caramel)}
p.body{font-size:15px;line-height:22px}

/* header */
.site-header{top:0;left:0;width:1200px;height:152px;background:var(--white)}
.site-header .brand{left:120px;top:50px;font-size:22px}
.call{left:560px;top:36px;width:300px;justify-content:flex-end;font-family:'Cinzel',serif;font-weight:700;font-size:19px;color:var(--ink);display:flex;align-items:center;gap:8px;white-space:nowrap}
.call span{color:var(--caramel)}
.schedule-top{left:876px;top:24px;width:196px;height:52px;line-height:52px;background:var(--olive);font-size:16px}
.main-nav{left:340px;top:100px;display:flex;gap:38px;font-family:'Cinzel',serif;font-size:15px;font-weight:600;color:var(--ink)}
.main-nav .active{color:var(--caramel)}

/* hero */
.hero{top:152px;left:0;width:1200px;height:760px;background:radial-gradient(ellipse at 55% 55%,#f0c166 0%,#b98a3c 12%,#4f5a26 38%,#2d3a18 70%,#1e2710 100%)}
.hero-text{top:390px;left:0;width:1200px;text-align:center;color:var(--white);font-family:'Cinzel',serif}
.hero-text .line1{font-size:32px;font-weight:600;letter-spacing:1px}
.hero-text .line2{font-size:60px;font-weight:600;letter-spacing:2px;line-height:70px}

/* about */
.about-title{left:128px;top:900px;font-size:44px;line-height:50px}
.about-text{left:128px;top:1030px;width:500px}
.about-btn{left:128px;top:1276px;width:152px;height:48px;line-height:48px}
.about-photo{left:656px;top:900px;width:340px;height:340px;border-radius:50%;background:radial-gradient(circle at 60% 35%,#f6d39a,#b98c4a 40%,#58612f 80%);border:8px solid var(--white);box-shadow:0 0 0 6px var(--olive)}

/* services */
.services{top:1390px;left:0;width:1200px;height:820px;background:var(--cream)}
.services-title{top:1500px;left:0;width:1200px;text-align:center;font-size:46px}
.service-row{top:1610px;left:118px;width:964px;display:flex;justify-content:space-between}
.service{width:172px;text-align:center;font-family:'Cinzel',serif;font-size:15px;line-height:19px;font-weight:600;color:var(--ink)}
.service svg{display:block;margin:0 auto 10px}
.service.active{color:var(--caramel)}
.arrow{top:1670px;font-size:34px;color:var(--ink);font-family:'Roboto',sans-serif}
.service-card{top:1808px;left:128px;width:944px;height:380px;background:var(--white);border-radius:14px;box-shadow:0 6px 24px rgba(0,0,0,.08)}
.service-card .heading{position:absolute;left:58px;top:50px;font-size:36px}
.service-card p{position:absolute;left:58px;top:112px;width:520px}
.service-card .btn{position:absolute;left:58px;top:280px;width:148px;height:48px;line-height:48px}
.card-photo{position:absolute;right:30px;top:26px;width:320px;height:320px;border-radius:10px;background:linear-gradient(135deg,#c9b79f,#8c7a62 50%,#3f3a2e)}

/* testimonials */
.testi-title{top:2280px;left:0;width:1200px;text-align:center;font-size:46px}
.avatar{border-radius:50%;background:radial-gradient(circle,#e2d6c6,#9d917f)}
.avatar.side{width:92px;height:92px;top:2420px;opacity:.7}
.avatar.main{width:136px;height:136px;top:2398px;left:532px;box-shadow:0 0 0 6px var(--white),0 0 0 8px var(--caramel)}
.testi-name{top:2564px;left:0;width:1200px;text-align:center;font-family:'Cinzel',serif;font-weight:700;font-size:16px;color:var(--ink)}
.testi-quote{top:2600px;left:280px;width:640px;text-align:center;font-style:italic;font-size:17px;line-height:24px;color:var(--ink)}
.dots{top:2752px;left:0;width:1200px;display:flex;justify-content:center;gap:10px}
.dots i{width:12px;height:12px;border-radius:50%;background:#d8d6d0}
.dots i.on{background:var(--caramel)}

/* consultation */
.consult{top:2806px;left:0;width:1200px;height:576px;background:linear-gradient(100deg,#8b6b3f 0%,#4f4a2a 35%,#2f3a22 65%,#26301c 100%)}
.consult-text{top:3050px;left:640px;width:520px;text-align:center;color:var(--white);font-family:'Cinzel',serif;font-weight:600;font-size:44px;line-height:50px}
.consult-btn{top:3238px;left:802px;width:196px;height:46px;line-height:42px;border:2px solid var(--white);background:var(--olive);font-size:15px}

/* videos */
.videos-title{top:3448px;left:0;width:1200px;text-align:center;font-size:46px}
.video{top:3566px;width:460px;height:274px;border-radius:12px}
.video.one{left:128px;background:linear-gradient(180deg,#cfd8d8,#9fb38a 45%,#4f6a2c)}
.video.two{left:612px;background:linear-gradient(180deg,#7e8a4a,#d9c28f 50%,#56632e)}
.play{position:absolute;left:50%;top:50%;transform:translate(-50%,-50%)}
.video-cap{top:3862px;width:460px;text-align:center;font-family:'Cinzel',serif;font-weight:700;font-size:17px;line-height:24px;color:var(--ink)}

/* contact */
.contact{top:4000px;left:0;width:1200px;height:660px;background:linear-gradient(180deg,#ffffff 0%,#ebe8e1 25%,#ddd9cf 100%)}
.contact-title{top:4196px;left:0;width:1200px;text-align:center;font-size:44px}
.field{background:var(--white);border-radius:8px;font-size:13px;color:var(--ink);padding:12px 20px}
.submit{top:4512px;left:512px;width:176px;height:54px;line-height:54px}

/* footer */
.footer{top:4640px;left:0;width:1200px;height:468px;background:var(--olive)}
.footer h3{font-family:'Cinzel',serif;font-weight:600;font-size:22px;color:var(--white)}
.footer .info{font-size:14px;color:#e9e7da;line-height:18px}
.f-item{display:flex;gap:14px;align-items:flex-start;margin-bottom:18px}
.f-icon{width:30px;height:30px;border-radius:50%;background:var(--caramel);flex:none}
.footer .brand{font-size:30px;color:var(--caramel);flex-direction:column;gap:12px}
.footer .brand .brand-dot{width:90px;height:90px}
.social{display:flex;gap:18px}
.social i{width:22px;height:22px;border-radius:50%;background:#e9e7da}
.copyright{top:5078px;left:0;width:1200px;text-align:center;font-size:13px;color:#e9e7da}
</style>
</head>
<body>

<header class="site-header abs">
  <div class="brand abs"><span class="brand-dot"></span>Quiet Harbor Path</div>
  <div class="call abs">
    <svg width="22" height="22" viewBox="0 0 24 24"><path fill="#3a3a32" d="M6.6 10.8a15 15 0 006.6 6.6l2.2-2.2c.3-.3.7-.4 1-.2 1.1.4 2.3.6 3.6.6.6 0 1 .4 1 1V20c0 .6-.4 1-1 1A17 17 0 013 4c0-.6.4-1 1-1h3.5c.6 0 1 .4 1 1 0 1.3.2 2.5.6 3.6.1.3 0 .7-.2 1z"/></svg>
    CALL US: <span>XXX 888-8888</span>
  </div>
  <a class="btn schedule-top abs">SCHEDULE NOW</a>
  <nav class="main-nav abs">
    <span class="active">HOME</span><span>ABOUT US</span><span>OUR SERVICES ▾</span><span>TESTIMONIALS</span><span>BLOG</span><span>CONTACT</span>
  </nav>
</header>

<section class="hero abs" role="img" aria-label="Sunlit forest with a wooden boardwalk path winding between mossy trees"></section>
<div class="hero-text abs">
  <div class="line1">QUIET HARBOR PATH– WHAT MIGHT YOU FIND...</div>
  <div class="line2">LESSONS SOLUTIONS ANSWERS</div>
</div>
<svg class="abs" style="top:780px;left:0" width="1200" height="140" viewBox="0 0 1200 140">
  <path d="M0 60 C300 150 700 150 1200 20 L1200 140 L0 140Z" fill="#ffffff"/>
  <path d="M0 60 C300 150 700 150 1200 20" fill="none" stroke="#e0862a" stroke-width="8"/>
</svg>

<h2 class="heading about-title abs">ABOUT<br>HYPNOTHERAPY</h2>
<p class="body about-text abs">Hypnosis gently opens the door to the subconscious mind, where the answers to living your best life already rest. Through calm, guided sessions we build new pathways in the brain that shape new behaviors and responses. Whether you seek relief from anxiety, freedom from old habits or insight from past lives and the life between lives, each session is tailored to you. Together we explore what lies beneath, so lasting change can take root and grow naturally.</p>
<a class="btn about-btn abs">READ MORE</a>
<div class="about-photo abs" role="img" aria-label="Woman relaxing in a sunny meadow with eyes closed"></div>

<section class="services abs"></section>
<svg class="abs" style="top:1340px;left:0" width="1200" height="60" viewBox="0 0 1200 60"><path d="M0 50 C400 0 800 0 1200 40 L1200 60 L0 60Z" fill="#efede8"/></svg>
<h2 class="heading services-title abs">OUR SERVICES</h2>
<div class="arrow abs" style="left:60px">‹</div>
<div class="arrow abs" style="left:1114px">›</div>
<div class="service-row abs">
  <div class="service active"><svg width="80" height="80" viewBox="0 0 80 80"><circle cx="40" cy="40" r="34" fill="none" stroke="#e0862a" stroke-width="3"/></svg>ANXIETY</div>
  <div class="service"><svg width="80" height="80" viewBox="0 0 80 80"><circle cx="40" cy="40" r="34" fill="none" stroke="#3a3a32" stroke-width="3"/><circle cx="40" cy="40" r="18" fill="none" stroke="#3a3a32" stroke-width="3"/></svg>PAIN RELIEF</div>
  <div class="service"><svg width="80" height="80" viewBox="0 0 80 80"><rect x="20" y="8" width="40" height="64" rx="18" fill="none" stroke="#3a3a32" stroke-width="3"/><line x1="10" y1="40" x2="70" y2="40" stroke="#3a3a32" stroke-width="3"/></svg>WEIGHT LOSS</div>
  <div class="service"><svg width="80" height="80" viewBox="0 0 80 80"><rect x="26" y="14" width="28" height="56" rx="6" fill="none" stroke="#3a3a32" stroke-width="3"/><line x1="16" y1="20" x2="64" y2="64" stroke="#3a3a32" stroke-width="3"/></svg>SMOKING/<br>VAPING CESSATION</div>
  <div class="service"><svg width="80" height="80" viewBox="0 0 80 80"><circle cx="40" cy="20" r="10" fill="none" stroke="#3a3a32" stroke-width="3"/><path d="M14 30 L40 38 L66 30 M40 38 V58 M40 58 L28 74 M40 58 L52 74" fill="none" stroke="#3a3a32" stroke-width="3"/></svg>SELF<br>CONFIDENCE</div>
</div>
<article class="service-card abs">
  <h3 class="heading">ANXIETY</h3>
  <p class="body">Anxiety can keep the mind racing long after the moment has passed. Hypnotherapy helps you reach a deep state of calm, where the patterns behind worry can be gently understood and reshaped. Sessions teach your body and mind to respond with ease instead of tension, giving you tools to return to stillness whenever you need. Many clients notice a lighter, steadier feeling after only a few visits.</p>
  <a class="btn">READ MORE</a>
  <div class="card-photo" role="img" aria-label="Close-up of hands clasped nervously in a lap"></div>
</article>

<h2 class="heading testi-title abs">TESTIMONIALS</h2>
<div class="avatar side abs" style="left:452px" role="img" aria-label="Client portrait"></div>
<div class="avatar side abs" style="left:656px" role="img" aria-label="Client portrait"></div>
<div class="avatar main abs" role="img" aria-label="Portrait of Maren, a smiling client"></div>
<div class="testi-name abs">MAREN</div>
<p class="testi-quote abs">"Lorem ipsum dolor sit amet, cons ectetur adipiscing elit, sed do eiusmod tempor incididunt ut labore et dolore magna aliqua. Quis ipsum suspendisse ultrices gravida. Risus commodo viverra maecenas accumsan lacus vel facilisis."</p>
<div class="dots abs"><i class="on"></i><i></i><i></i><i></i><i></i></div>

<section class="consult abs" role="img" aria-label="Woman with curly hair gently blowing a dandelion seed head in warm evening light"></section>
<svg class="abs" style="top:2780px;left:0" width="1200" height="60" viewBox="0 0 1200 60"><path d="M0 0 H1200 V10 C800 60 400 60 0 26Z" fill="#ffffff"/></svg>
<h2 class="consult-text abs">BOOK YOUR FREE<br>CONSULTATION NOW</h2>
<a class="btn consult-btn abs">SCHEDULE NOW</a>
<svg class="abs" style="top:3330px;left:0" width="1200" height="60" viewBox="0 0 1200 60"><path d="M0 60 V30 C400 0 800 0 1200 40 V60Z" fill="#ffffff"/></svg>

<h2 class="heading videos-title abs">OUR VIDEOS</h2>
<div class="video one abs" role="img" aria-label="Person with arms raised in a green mountain meadow">
  <svg class="play" width="74" height="74" viewBox="0 0 74 74"><circle cx="37" cy="37" r="34" fill="rgba(255,255,255,.35)" stroke="#fff" stroke-width="3"/><path d="M30 24 L52 37 L30 50Z" fill="#fff"/></svg>
</div>
<div class="video two abs" role="img" aria-label="Smiling woman in a sunny forest clearing">
  <svg class="play" width="74" height="74" viewBox="0 0 74 74"><circle cx="37" cy="37" r="34" fill="rgba(255,255,255,.35)" stroke="#fff" stroke-width="3"/><path d="M30 24 L52 37 L30 50Z" fill="#fff"/></svg>
</div>
<div class="video-cap abs" style="left:128px">LOREM IPSUM DOLOR SIT AMET,<br>CONSECTETUR ADIPISCING</div>
<div class="video-cap abs" style="left:612px">LOREM IPSUM DOLOR SIT AMET,<br>CONSECTETUR ADIPISCING</div>

<section class="contact abs" role="img" aria-label="Soft sandy beach with seashells in muted light"></section>
<h2 class="heading contact-title abs">HOW TO CONTACT US</h2>
<div class="field abs" style="top:4300px;left:248px;width:340px;height:50px">Name</div>
<div class="field abs" style="top:4364px;left:248px;width:340px;height:50px">Email</div>
<div class="field abs" style="top:4428px;left:248px;width:340px;height:50px">Phone</div>
<div class="field abs" style="top:4300px;left:604px;width:336px;height:178px">Message</div>
<a class="btn submit abs">SUBMIT NOW</a>

<svg class="abs" style="top:4590px;left:0" width="1200" height="110" viewBox="0 0 1200 110">
  <path d="M0 40 C400 110 800 110 1200 30 V110 H0Z" fill="#5b5a2c"/>
  <path d="M0 40 C400 110 800 110 1200 30" fill="none" stroke="#e0862a" stroke-width="8"/>
</svg>
<footer class="footer abs">
  <div class="abs" style="left:128px;top:52px;width:300px">
    <h3 style="margin-bottom:26px">CONTACT US</h3>
    <div class="f-item"><span class="f-icon"></span><div class="info">P.O. Box XXX Lorem XXX<br>Location Name XXX</div></div>
    <div class="f-item"><span class="f-icon"></span><div class="info">Phone<br>XXX 777 140 120</div></div>
    <div class="f-item"><span class="f-icon"></span><div class="info">Email<br>info@quietharborpath.example</div></div>
  </div>
  <div class="brand abs" style="left:400px;top:80px;width:400px">
    <span class="brand-dot"></span>Quiet Harbor Path
  </div>
  <div class="social abs" style="left:526px;top:290px"><i></i><i></i><i></i><i></i></div>
  <div class="abs" style="left:840px;top:52px;width:232px;text-align:right">
    <h3 style="margin-bottom:26px">ABOUT US</h3>
    <p class="info">Calm, caring hypnotherapy for lasting change. We guide you to the answers within, through past life and life between lives work.</p>
  </div>
</footer>
<div class="copyright abs">Copyright © 2024 Quiet Harbor Path · All rights reserved</div>

</body>
</html>
```